Digital Imaging Website Design Project

This project is for 3 page designs - The main Home page design, department page design & content page design which will utilize most of the home page components.

Client Background - http://www.kelrofab.com

An almost Forty year old established printing company that has a large client base of architect/engineering, as the print shop opened up as a blueprinting company, and over the years has grown, changed and expanded to offer document and digital file management for this industry. KRFab. has also always offered color printing services, but recently has expanded their color department to be able to offer amazing dimensional printing, and extreme cutting technology.

These new products and services will be targeted to new industries for repeatable printing needs, promotional, point of purchase color printing, as well as in-store, interior decor/wall. These new printing services are only offered by KRFAB in their area, and they want to convey that they are on the leading edge of color printing technology, while at the same time, not eliminating their existing primary business scaring away their traditional client base of architectural/engineering firms that use them for large format printing, scanning and document management services.

1 - Home Page Design
Primary Goals of the design:

1.Provide a new, eye catching engaging website that conveys the above expansion/growth/cutting edge company.
2.Full screen design please to move away from the 'center' bordered up website they currently have.
3.Design Components – We don't have any media to provide you with exception of our logo. We're looking for fresh design that is exciting and engaging imagery. Additionally, we are working on a color/effected version of our logo to place on the color division page, and this will probably tie in with the design you create for us.
4.It should be designed to be able to work as a responsive design as well so that when installed, will work across devices etc..
5.Colors – Same color scheme, but if you have an accent color you'd like to use to make the site pop, go for it!

Requirements:
1.The 4 divisions of the company should be the main feature so that the client depending on which department they are needing, will see those 4 choices clearly in the design, and they'll know to click on one of them to get more information and to their needed services.

2.The main goal of the site is to get visitors to place an order, there should be a feature on the home page for this call to action.

3.Put in an element that communicates the main benefit of KRFab. - an area for a 1-line Statement/Call to Action / Overall Company Benefit/

4.The 4 divisions need to have eye catching elements related to their products and services, and that clearly illustrate that the user should click on that to go to the appropriate area for products and services

Reprographics
This department is specifically geared to architect/engineering industry
BYLine for optional Use: Partnering with Building Industry Providers since 1975
Related pages for better understanding:
http://www.kelrofab.com/services/portland_professional_printing_services
http://www.kelrofab.com/services/reprographics
Digital File Management
This department is related to Architect/engineers, but can also apply to any other industry needing electronic document management, scanning, or archival services.
BYLine for optional use: Effective & Efficient Digital Solutions at every level.
Related Pages:
http://www.kelrofab.com/colorgraphics/electronic_file_document_management
http://www.kelrofab.com/colorgraphics/document_scanning_service
http://www.kelrofab.com/services/scanning_and_archiving

Color Graphics
This Department is newly expanded / has expanded services / they are focusing more of their efforts on this department and is a key reason for updated website design.
This Department image/representation should be stellar in the imagery to convey the excellence of the color department the services availble.
One of their newest products/services is dimensional printing – not 3-D, but raised element printing. Essentially a client could pick components on their graphic that that they want to 'bump' out, and additional layers would be put in place to create a popped out, dimensional effect. * Bonus points for creating the color department image that effectively conveys this new service – whether it's showing an abstract image/element that is actually raised off the page/paper/component. Additionally the color dimensional printing can be done on practically any material – glass, vinyl, material etc.... Please let me know if you have any questions on this.
BYLine for optional Use: See How Our Color Stands Out From the Rest
Related pages:
http://www.kelrofab.com/colorgraphics
http://www.kelrofab.com/colorgraphics/color_digital_imaging

Equipment & Supplies
This department provides specific supplies and hardware vs. printing products/services. Our largest client base is architects/engineers, but is not limited to this industry. Typical equipment is large printers, and supplies are typically paper products geared to the large format printing services, for the architect/engineers industry.
Byline for optional Use: In-House Printing & Fulfillment Services
Related pages:
http://www.kelrofab.com/varlen_tusk_equipment_sales
http://www.kelrofab.com/supplies

Additionally - Possibly have descriptive text sections below these 4 elements, but this is optional.

2.) Department/Division Page design -

This page should pull the home page element to over based on which division is selected.
Have a submenu design incorporated so that users can navigate to all the products and services that will be listed under that division
Contain a plugin design for FAQs – so that depending on which division page they are on, the appropriate FAQ's would display for use to have easy access to.
Contain a plugin design for – Contact Us easy form – short form –
Name
Company
Number
Email
Project Details/Questions: Text box

3.)Content Page design
This page should have main area for content
Area for an image with slideshow of other supporting images
Optional area for video – most (99%) of the pages will not have videos, but in the case we do, would like an area that will display videos effectively.
Optional FAQ plugin display
Contact plugin display

Global Elements:

Static and very visible site features that are in a position so that if user clicks beyond home page will still see these are:
Get a Quote
Place Order
Digital Plan-room
Call Today - 503-481-7962

Other global components:
SM Icons – QN, Chirpo, WorkLoop
Rotating Testimonial

Navigational Menu:
The KRF Difference
About
Sustainability
Products & Services
Reprograhics
Digital File Management
Color Graphics
Equipment & Supplies
Login
Blog
Contact Us

After the contest – What would be great to have is when a user clicks on one of the departments, it takes that visual element and continues onto it's department page for a smaller but related image - But this may be an after this web design contest.

Additionally will need some other design work on the interior pages, as well, so hoping to find a great designer to complete the other tasks – as well as be the go-to for future endeavors!

Thanks for looking at the project, and I look forward to any questions you may have.
Updates

Looking forward to hearing from interested designers! - If you're curious about my work, you can find my profile at:  https://www.gigmarla.com/users/~07b3e2f95d18c4a260

Target Market(s)

Please see description

Industry/Entity Type

Electronic

Requirements
Must have
• Please see description

```html
<!DOCTYPE html>
<html lang="en">
<head>
<meta charset="utf-8">
<title>KRF Digital Imaging – Home</title>
<link rel="stylesheet" href="https://fonts.googleapis.com/css2?family=Open+Sans:ital,wght@0,400;0,600;0,700;1,400&family=Ubuntu:wght@300;400&display=swap">
<style>
:root{
  --navy:#27318c;
  --nav-top:#3553b4;
  --nav-bottom:#1d2f82;
  --orange:#f57f2a;
  --orange-dark:#e0641a;
  --text-grey:#9a9a9a;
  --text-dark:#333;
  --rule:#d6d6d6;
  --btn-dark:#1e1e1e;
  --band:#ececec;
  --green:#5bb031;
}
*{box-sizing:border-box;margin:0;padding:0}
html,body{width:721px;height:1200px;overflow:hidden;background:#fff}
body{position:relative;font-family:"Open Sans",Arial,sans-serif;color:var(--text-dark)}
.abs{position:absolute}

/* header */
.brand{left:14px;top:12px;display:flex;align-items:center;gap:10px}
.brand-mark{width:16px;height:16px;background:var(--navy)}
.brand-name{font-family:"Open Sans",Arial,sans-serif;font-weight:700;color:var(--navy);font-size:15px;line-height:17px;letter-spacing:.3px}
.brand-tag{left:40px;top:56px;font-size:9px;font-style:italic;color:var(--navy)}
.call{right:14px;top:14px;display:flex;align-items:center;gap:10px;font-size:12px;color:#9a9a9a;letter-spacing:.4px}
.call-icon{width:22px;height:22px}
.utility{right:12px;top:47px;display:flex;gap:4px}
.util-btn{height:19px;padding:0 6px;border:1px solid #c9c9c9;background:linear-gradient(#fff,#e6e6e6);font-size:9.5px;color:#222;display:flex;align-items:center;gap:4px}
.util-btn.login{background:linear-gradient(#fa9a4a,var(--orange-dark));border-color:var(--orange-dark);color:#fff;padding:0 10px}
.tri{width:0;height:0;border-left:4px solid currentColor;border-top:3.5px solid transparent;border-bottom:3.5px solid transparent}

/* nav */
.main-nav{left:0;top:83px;width:721px;height:30px;background:linear-gradient(var(--nav-top),var(--nav-bottom));display:flex}
.main-nav a{color:#fff;text-decoration:none;font-size:11.5px;display:flex;align-items:center;justify-content:center;border-left:1px solid rgba(255,255,255,.45);flex:auto}
.main-nav a:first-child{border-left:none}

/* hero */
.hero{left:0;top:122px;width:721px;height:193px;background:linear-gradient(90deg,#e6e6e6,#f4f4f4 50%,#ececec)}
.hero-visual{left:0;top:0;width:304px;height:193px;background:linear-gradient(135deg,#f4f8fc,#c6d7ea 55%,#8fb0d6)}
.hero-title{left:352px;top:42px;font-family:"Ubuntu",sans-serif;font-weight:300;font-size:28px;line-height:36px;color:var(--navy)}
.btn-orange{left:357px;top:133px;width:85px;height:23px;background:linear-gradient(#fb9b4c,var(--orange-dark));color:#fff;font-size:11px;font-weight:600;display:flex;align-items:center;justify-content:center;gap:5px;border-radius:2px}
.dots{left:329px;top:328px;display:flex;gap:7px}
.dots span{width:9px;height:9px;border-radius:50%;background:#d4d4d4}
.dots span:first-child{background:#2c44a4}
.dotted{height:0;border-top:1px dotted #bdbdbd}

/* divisions */
.division{top:364px;width:166px}
.division h2{font-family:"Ubuntu",sans-serif;font-weight:400;font-size:18px;line-height:24px;color:var(--navy);height:54px;text-transform:uppercase}
.division .thumb{width:152px;height:90px;border:1px solid #e2e2e2;padding:4px;margin-top:2px}
.division .thumb div{width:100%;height:100%}
.division p{font-size:10px;line-height:15px;color:var(--text-grey);margin-top:10px;width:158px}
.division p + p{margin-top:15px}
.btn-dark{height:21px;width:78px;background:var(--btn-dark);color:#fff;border-radius:4px;font-size:10px;display:flex;align-items:center;gap:6px;padding-left:9px}
.btn-dark .play{width:11px;height:11px;border-radius:50%;background:#fff;display:flex;align-items:center;justify-content:center;color:#111}
.btn-dark .play i{border-left:4px solid #111;border-top:3px solid transparent;border-bottom:3px solid transparent;margin-left:1px}
.vrule{width:0;border-left:1px dotted #c4c4c4}

/* about & testimonials */
.section-label{font-family:"Open Sans",Arial,sans-serif;font-weight:400;font-size:12.5px;color:#333;letter-spacing:.6px;text-transform:uppercase}
.about-photo{left:20px;top:742px;width:178px;height:138px;background:linear-gradient(180deg,#fff 0%,#e2e4e8 40%,#3a3f4a 100%);border-radius:2px}
.about-text{left:221px;top:742px;width:258px;font-size:10px;line-height:15.5px;color:var(--text-grey)}
.about-text p + p{margin-top:14px}
.testimonials{left:507px;top:729px;width:200px}
.testimonials h3{font-family:"Ubuntu",sans-serif;font-weight:400;font-size:14px;letter-spacing:.5px;color:#333;text-transform:uppercase}
.testimonials p{font-size:9px;line-height:15px;color:var(--text-grey);margin-top:14px}
.testimonials .date{font-size:10px;color:#222;margin-top:6px;font-weight:600}
.pager{left:650px;top:892px;display:flex;gap:4px}
.pager span{width:22px;height:21px;border:1px solid #bbb;border-radius:3px;background:linear-gradient(#fff,#e4e4e4);display:flex;align-items:center;justify-content:center}

/* equipment */
.equip-band{left:0;top:958px;width:721px;height:132px;background:linear-gradient(#f7f7f7,var(--band))}
.equip-item{top:968px;width:131px;height:110px;border:1px solid #555;background:#fff;display:flex;align-items:center;justify-content:center}
.equip-item div{width:100px;height:80px;background:linear-gradient(#eaeaea,#9b9b9b);border-radius:3px}
.arrow-circle{top:1016px;width:17px;height:17px;border-radius:50%;border:1px solid #888;background:#fff;display:flex;align-items:center;justify-content:center}

/* footer */
.footer-links{left:0;top:1130px;width:721px;text-align:center;font-size:10.5px;letter-spacing:.4px;color:#222}
.footer-bar{left:0;top:1163px;width:721px;height:37px;background:linear-gradient(var(--nav-top),var(--nav-bottom))}
.copyright{left:12px;top:13px;font-size:9px;color:#fff}
.social{right:12px;top:7px;display:flex;gap:5px}
.social span{width:22px;height:22px;background:#e9e9e9;border-radius:2px}
</style>
</head>
<body>

<header>
  <div class="abs brand">
    <span class="brand-mark"></span>
    <span class="brand-name">KELRO PRINT &amp; REPROGRAPHIC<br>COMPANY, INC.</span>
  </div>
  <div class="abs brand-tag">Precision Printing Partner Since 1982</div>

  <div class="abs call">
    <svg class="call-icon" viewBox="0 0 22 22" aria-hidden="true">
      <circle cx="11" cy="11" r="11" fill="var(--green)"/>
      <path d="M7.5 6.5c.6-.6 1.3-.5 1.7.1l1 1.6c.3.5.2 1-.2 1.4l-.6.6c.5 1.1 1.3 1.9 2.4 2.4l.6-.6c.4-.4.9-.5 1.4-.2l1.6 1c.6.4.7 1.1.1 1.7l-.8.8c-.8.8-4 .2-6.2-2s-2.8-5.4-2-6.2z" fill="#fff"/>
    </svg>
    <span>Call Today – 503-481-7962</span>
  </div>

  <div class="abs utility">
    <span class="util-btn"><i class="tri"></i>Digital Plan Room</span>
    <span class="util-btn"><i class="tri"></i>Place Order</span>
    <span class="util-btn"><i class="tri"></i>Get a Quote</span>
    <span class="util-btn login"><i class="tri"></i>Login</span>
  </div>
</header>

<nav class="abs main-nav">
  <a href="#">The KRF Difference</a>
  <a href="#">About</a>
  <a href="#">Sustainability</a>
  <a href="#">Products &amp; Services</a>
  <a href="#">Reprograhics</a>
  <a href="#">Digital File Management</a>
  <a href="#">Color Graphics</a>
  <a href="#">Blog</a>
  <a href="#">Contact</a>
</nav>

<section class="abs hero">
  <div class="abs hero-visual" role="img" aria-label="Architectural blueprints with a pen and ruler"></div>
  <h1 class="abs hero-title">Services For Architects,<br>Engineers And Builders</h1>
  <div class="abs btn-orange"><i class="tri"></i>View More</div>
</section>
<div class="abs dots"><span></span><span></span><span></span><span></span></div>
<div class="abs dotted" style="left:12px;top:352px;width:697px"></div>

<section class="divisions">
  <article class="abs division" style="left:12px">
    <h2>Repro<br>Graphics</h2>
    <div class="thumb"><div role="img" aria-label="Rolled architectural plans" style="background:linear-gradient(135deg,#eef4fb,#9fc2e8 60%,#5d8fd0)"></div></div>
    <p>Donec quam felis, ultricies nec, pellentesq ue eu, pretium quis, sem. Nulla consequat massa quis enim. Donec pede justo, fri ngilla vel, aliquet.</p>
    <p>In enim justo, rhoncus ut, im-perdiet a, venenatis vitae.</p>
  </article>
  <div class="abs btn-dark" style="left:12px;top:659px"><span class="play"><i></i></span>View More</div>
  <div class="abs vrule" style="left:178px;top:366px;height:314px"></div>

  <article class="abs division" style="left:192px">
    <h2 style="line-height:21px">Digital File<br>Management</h2>
    <div class="thumb"><div role="img" aria-label="Wall of digital document screens" style="background:linear-gradient(135deg,#0f1d4a,#3a5fa8 55%,#1a2a5e)"></div></div>
    <p>Donec quam felis, ultricies nec, pellentesq ue eu, pretium quis, sem. Nulla consequat massa quis enim. Donec pede justo, fri ngilla vel, aliquet.</p>
    <p>In enim justo, rhoncus ut, im-perdi tenenatis jitae.</p>
  </article>
  <div class="abs btn-dark" style="left:192px;top:659px"><span class="play"><i></i></span>View More</div>
  <div class="abs vrule" style="left:361px;top:366px;height:314px"></div>

  <article class="abs division" style="left:376px">
    <h2>Color<br>Graphics</h2>
    <div class="thumb"><div role="img" aria-label="Vivid multicolour abstract artwork" style="background:linear-gradient(90deg,#f0c020,#e43a6b 30%,#7a3fb8 55%,#1aa0d8 80%,#55c040)"></div></div>
    <p>Donec quam felis, ultricies nec, pellentesq ue eu, pretium quis, sem. Nulla consequat massa quis enim. Donec pede justo, fri ngilla vel, aliquet.</p>
    <p>In enim justo, rhoncus ut, im-perdi nenatis iutae.</p>
  </article>
  <div class="abs btn-dark" style="left:376px;top:659px"><span class="play"><i></i></span>View More</div>
  <div class="abs vrule" style="left:544px;top:366px;height:314px"></div>

  <article class="abs division" style="left:560px">
    <h2>Equipment &amp;<br>Supplies</h2>
    <div class="thumb"><div role="img" aria-label="Large format printers" style="background:linear-gradient(#f4f4f4,#bdbdbd)"></div></div>
    <p>Donec quam felis, ultricies nec, pellentesq ue eu, pretium quis, sem. Nulla consequat massa quis enim. Donec pede justo, fri ngilla vel, aliquet.</p>
    <p>In enim justo, rhoncus ut, impe fsdos fgrhae.</p>
  </article>
  <div class="abs btn-dark" style="left:560px;top:659px"><span class="play"><i></i></span>View More</div>
</section>

<div class="abs dotted" style="left:12px;top:700px;width:697px"></div>

<section class="about">
  <h3 class="abs section-label" style="left:20px;top:716px">About Us</h3>
  <div class="abs about-photo" role="img" aria-label="Team of business professionals"></div>
  <div class="abs about-text">
    <p>Donec quam felis, ultricies nec, pellentesq ue eu, pretium quis, sem. Nulla consequat massa quis enim, eonec pede justo, fri ngilla vel, aliquet. In enim justo, rhoncus ut, imperdiet a, venenatis vitae, juollis rhoncus ut, imperdiet a, venenatis vitretium.</p>
    <p>Tonec quam felis, ultricies nec, pellentesq ue eu, pretium quis, sem.</p>
  </div>
  <div class="abs btn-dark" style="left:221px;top:885px"><span class="play"><i></i></span>View More</div>
</section>

<div class="abs vrule" style="left:484px;top:722px;height:182px"></div>

<aside class="abs testimonials">
  <h3>Testimonials</h3>
  <p>Quisque rutrum. Aenean imperdiet. Etiam ultricies nisi vel augue. Curabitur ullamcor-per ultricies nisi.</p>
  <div class="date">12 Aug 2013</div>
  <p>Quisque rutrum. Aenean imperdiet. Etiam ultricies nisi vel augue.</p>
  <div class="date">11 Aug 2013</div>
</aside>
<div class="abs pager">
  <span><svg width="8" height="9" viewBox="0 0 8 9"><path d="M6 0v9L0 4.5z" fill="#444"/></svg></span>
  <span><svg width="8" height="9" viewBox="0 0 8 9"><path d="M2 0v9l6-4.5z" fill="#444"/></svg></span>
</div>

<div class="abs dotted" style="left:12px;top:922px;width:697px"></div>

<section class="equipment">
  <h3 class="abs section-label" style="left:20px;top:933px">Equipment Sales</h3>
  <div class="abs equip-band"></div>
  <div class="abs arrow-circle" style="left:12px"><svg width="6" height="7" viewBox="0 0 6 7"><path d="M5 0v7L0 3.5z" fill="#555"/></svg></div>
  <div class="abs equip-item" style="left:42px"><div role="img" aria-label="Wide format printer"></div></div>
  <div class="abs equip-item" style="left:211px"><div role="img" aria-label="Production colour printer"></div></div>
  <div class="abs equip-item" style="left:380px"><div role="img" aria-label="Large format plotter"></div></div>
  <div class="abs equip-item" style="left:550px"><div role="img" aria-label="Multifunction plan printer"></div></div>
  <div class="abs arrow-circle" style="left:691px"><svg width="6" height="7" viewBox="0 0 6 7"><path d="M1 0v7l5-3.5z" fill="#555"/></svg></div>
</section>

<div class="abs" style="left:0;top:1112px;width:721px;border-top:1px solid #ddd"></div>

<footer>
  <div class="abs footer-links">Home | Service | Color Graphics | Equipment Sales | Supplies | About Us | Contact Us</div>
  <div class="abs footer-bar">
    <div class="abs copyright">Copyright © 2013 KRF DIGITAL IMAGING</div>
    <div class="abs social" aria-label="Social links"><span></span><span></span><span></span><span></span><span></span></div>
  </div>
</footer>

</body>
</html>
```